Join Wait / Reservations Handout

This is a handout for guests with information about the ability to join our
waitlist and/or make reservations. It will be handed out to any guest that ends up waiting on our waitlist to be seated. It will describe how our waitlist and reservations system works. It is informational for them to download our mobile app.

It was forcing me to move the look and feel sliders. Please refer to our branding guide for look and feel.

Industry/Entity Type

Hospitality

Contact Information for Business Card

One of the attached documents give a very generic layout of the information we need on this card. This layout is more for where we wanted the information placed and has nothing to do with the design aspects of the piece. Please use your imagination. Any of the 5 colors in the branding guide can be used anywhere. The pineapple design can be used anywhere in any color combination.

If you require any other files please let me know. Thanks

Font styles to use
Other font styles liked:
• Please see attached branding guide

Requirements
Must have
• The only color requirement is that the logo be the blue with teal lettering...This has to match our app store logo.

```html
<!DOCTYPE html>
<html lang="en">
<head>
<meta charset="utf-8">
<title>Join Wait / Reservations Handout</title>
<link href="https://fonts.googleapis.com/css2?family=Jost:wght@400;500&family=Dancing+Script:wght@500&display=swap" rel="stylesheet">
<style>
  :root {
    --backdrop: #e3e3e3;
    --card-navy: #0c3b4f;
    --frame-line: #55808c;
    --gold: #e3a72b;
    --teal: #72b6b4;
    --blush: #e9a49b;
    --ink-light: #e4ecee;
  }
  * { box-sizing: border-box; margin: 0; padding: 0; }
  html, body { width: 1200px; height: 799px; overflow: hidden; }
  body {
    background: var(--backdrop);
    font-family: "Jost", "Futura", sans-serif;
    position: relative;
  }
  .card {
    position: absolute;
    top: 67px;
    width: 380px;
    height: 665px;
    background: var(--card-navy);
    box-shadow: 0 10px 24px rgba(0,0,0,.18);
  }
  .card--front { left: 180px; }
  .card--back { left: 640px; }
  .card__frame {
    position: absolute;
    inset: 20px;
    border: 1px solid var(--frame-line);
  }

  /* Front */
  .tagline {
    position: absolute; top: 50px; left: 0; right: 0;
    text-align: center;
    font-family: "Dancing Script", cursive;
    font-weight: 500;
    font-size: 50px;
    color: var(--ink-light);
  }
  .app-call__rule {
    position: absolute; left: 60px; right: 60px;
    height: 1px; background: var(--gold);
  }
  .app-call__rule--top { top: 122px; }
  .app-call__rule--bottom { top: 166px; }
  .app-call {
    position: absolute; top: 130px; left: 0; right: 0;
    text-align: center;
    font-size: 19px; letter-spacing: 1px;
    color: var(--gold);
  }
  .brand-box {
    position: absolute; top: 215px; left: 90px;
    width: 200px; height: 200px;
    border: 1px solid var(--teal);
    display: flex; flex-direction: column;
    align-items: center; justify-content: center; gap: 14px;
  }
  .brand-box__mark {
    width: 22px; height: 22px; background: var(--teal);
  }
  .brand-box__name {
    font-size: 26px; font-weight: 500; letter-spacing: 2px;
    color: var(--teal); text-align: center; line-height: 1.15;
  }
  .search-cue {
    position: absolute; top: 468px; left: 0; right: 0;
    display: flex; justify-content: center; align-items: center; gap: 8px;
    color: var(--teal); font-size: 16px; font-weight: 500; letter-spacing: 1px;
  }
  .search-query {
    position: absolute; top: 560px; left: 0; right: 0;
    text-align: center;
    font-size: 18px; letter-spacing: 1px;
    color: var(--gold);
  }

  /* Back */
  .info-list {
    position: absolute; top: 46px; bottom: 46px; left: 44px; right: 44px;
    list-style: none;
    display: flex; flex-direction: column; justify-content: space-between;
  }
  .info-item { text-align: center; }
  .info-item__title { font-size: 20px; letter-spacing: 1px; }
  .info-item__notch { display: block; width: 100%; height: 14px; margin: 3px 0 10px; }
  .info-item__detail { font-size: 17px; color: var(--ink-light); line-height: 1.3; }
  .info-item__note { font-size: 12px; color: var(--ink-light); }
  .info-item__rule { height: 1px; margin-top: 18px; }
  .info-item--gold .info-item__title { color: var(--gold); }
  .info-item--gold .info-item__notch { stroke: var(--gold); }
  .info-item--gold .info-item__rule { background: var(--gold); }
  .info-item--teal .info-item__title { color: var(--teal); }
  .info-item--teal .info-item__notch { stroke: var(--teal); }
  .info-item--teal .info-item__rule { background: var(--teal); }
  .info-item--blush .info-item__title { color: var(--blush); }
  .info-item--blush .info-item__notch { stroke: var(--blush); }
  .info-item--blush .info-item__rule { background: var(--blush); }
</style>
</head>
<body>
  <section class="card card--front">
    <div class="card__frame"></div>
    <p class="tagline">save the wait</p>
    <div class="app-call__rule app-call__rule--top"></div>
    <p class="app-call">DOWNLOAD OUR APP</p>
    <div class="app-call__rule app-call__rule--bottom"></div>
    <div class="brand-box">
      <span class="brand-box__mark"></span>
      <span class="brand-box__name">MERIDIAN</span>
    </div>
    <div class="search-cue">
      <svg width="36" height="36" viewBox="0 0 34 34" aria-hidden="true">
        <circle cx="14" cy="14" r="10" fill="none" stroke="var(--teal)" stroke-width="4"/>
        <line x1="21" y1="21" x2="31" y2="31" stroke="var(--teal)" stroke-width="5" stroke-linecap="round"/>
      </svg>
      <span>SEARCH</span>
    </div>
    <p class="search-query">“MERIDIAN MILLBROOK”</p>
  </section>

  <section class="card card--back">
    <div class="card__frame"></div>
    <ul class="info-list">
      <li class="info-item info-item--gold">
        <p class="info-item__title">WHEN TO JOIN WAIT?</p>
        <svg class="info-item__notch" viewBox="0 0 292 14" preserveAspectRatio="none" aria-hidden="true"><polyline points="0,2 136,2 146,12 156,2 292,2" fill="none" stroke-width="1.2"/></svg>
        <p class="info-item__detail">Anytime</p>
        <div class="info-item__rule"></div>
      </li>
      <li class="info-item info-item--teal">
        <p class="info-item__title">WHEN TO RESERVE?</p>
        <svg class="info-item__notch" viewBox="0 0 292 14" preserveAspectRatio="none" aria-hidden="true"><polyline points="0,2 136,2 146,12 156,2 292,2" fill="none" stroke-width="1.2"/></svg>
        <p class="info-item__detail">Anytime - 2hours in Advance</p>
        <p class="info-item__note">(excluding weekend, open - 2pm)</p>
        <div class="info-item__rule"></div>
      </li>
      <li class="info-item info-item--teal">
        <p class="info-item__title">SUNDAY + HOLIDAY BUFFETS</p>
        <svg class="info-item__notch" viewBox="0 0 292 14" preserveAspectRatio="none" aria-hidden="true"><polyline points="0,2 136,2 146,12 156,2 292,2" fill="none" stroke-width="1.2"/></svg>
        <p class="info-item__detail">Coming JUNE</p>
        <div class="info-item__rule"></div>
      </li>
      <li class="info-item info-item--blush">
        <p class="info-item__title">LARGE GROUPS</p>
        <svg class="info-item__notch" viewBox="0 0 292 14" preserveAspectRatio="none" aria-hidden="true"><polyline points="0,2 136,2 146,12 156,2 292,2" fill="none" stroke-width="1.2"/></svg>
        <p class="info-item__detail">Handled/Contacted by<br>Catering Manager</p>
        <div class="info-item__rule"></div>
      </li>
    </ul>
  </section>
</body>
</html>
```